Pamphlet design, flyer, and poster for cardiology office

Hello design experts out there. We are looking for the following:
1. Brochure : accordian Z fold design.
2. Company folder with content (see pamphlet idea and design example.
3. Large pull up poster/banner.

They are used promote our Cardiology office.

The services our office provide are labelled 1-6 below.

A. For the company folder, please create a front and back insert x 3 that is staggered (see pamphlet idea, sunday; and small-medium-large, Monday) and inserted on the right side. Our referral form that has been designed and will be included on the left (referral BCC Monday). Feel free to use the same themes.
Inserts in folder:
• 1. Echocardiogram and 2. Stress Echocardiogram (largest page front and back)
• 3. Holter/Loop monitor and 4. Ambulatory blood pressure monitoring (medium sized page front and back)
• 5. Electrocardiogram and 6. Cardiac Consultations (smallest page front and back)

In terms of content for the folder inserts, our word content will likely not be more than 2 or 3 sentences (we are drafting them now). Please ensure colorful and attractive graphics are used to highlight these tests. Please use, where possible, pictures of tests more than of people. The goal is to emphasize the role of the office as a testing center. Feel free to look them up online (eg. Echo, stress echo, Holter monitoring etc).

B. For the accordian Z fold brochure, please design it such where by each item we offer (from 1-6 below) occupy 1 page of fold, with the exception where item 5 - 6 combined into 1 page. The front page of course will be the office logo and address etc.

C. For the Large pull up poster display for BRAMLEY CARDIAC CENTRE - simple, with picture. Dimensions 33" x 81"
This banner will have our logo, and a summary of ll the services we provide (1 - 6)

Items need to be graphics heavy and attractive as we are trying to avoid making it wordy.

Target Market(s)

Referring physicians, patietns

Industry/Entity Type

Health Care

Requirements
Must have
• Attractive graphics and pictures.
• Most graphics emphasize diagnostic testing we do.
Should not have
• Too much word content

```html
<!DOCTYPE html>
<html lang="en">
<head>
<meta charset="utf-8">
<title>Bramley Cardiac Centre – Pull-up Banner</title>
<link rel="stylesheet" href="https://fonts.googleapis.com/css2?family=Oswald:wght@400;500&display=swap">
<style>
  :root {
    --page-bg: #f2f2f2;
    --navy: #1b3566;
    --blue: #1f7fc6;
    --blue-deep: #173b7a;
    --red: #b3172c;
    --red-deep: #8e0f20;
    --panel: #eef0f2;
    --text-dark: #2b2b2b;
    --white: #ffffff;
  }
  * { box-sizing: border-box; margin: 0; padding: 0; }
  html, body {
    width: 1200px;
    height: 720px;
    overflow: hidden;
    background: var(--page-bg);
  }
  .canvas {
    position: relative;
    width: 1200px;
    height: 720px;
  }
  .banner {
    position: absolute;
    left: 462px;
    top: 20px;
    width: 276px;
    height: 680px;
    background: var(--panel);
    overflow: hidden;
    font-family: "Oswald", "Arial Narrow", sans-serif;
  }
  .banner-shapes {
    position: absolute;
    inset: 0;
    width: 276px;
    height: 680px;
  }
  .brand-name {
    position: absolute;
    left: 0;
    width: 276px;
    top: 96px;
    text-align: center;
    color: var(--navy);
    font-weight: 500;
    font-size: 22px;
    line-height: 1.05;
    letter-spacing: 0.5px;
    display: flex;
    align-items: center;
    justify-content: center;
    gap: 8px;
  }
  .brand-dot {
    width: 12px;
    height: 12px;
    border-radius: 50%;
    background: var(--red);
    flex: none;
  }
  .service-list {
    position: absolute;
    left: 68px;
    top: 488px;
    list-style: none;
    color: var(--text-dark);
    font-weight: 400;
    font-size: 15.5px;
    line-height: 1.0;
    text-transform: uppercase;
  }
  .service-list li {
    position: relative;
    padding-left: 0;
    margin-bottom: 6.5px;
  }
  .service-list li::before {
    content: "";
    position: absolute;
    left: -17px;
    top: 3px;
    width: 10px;
    height: 10px;
    border-radius: 50%;
    background: var(--red);
  }
  .footer-name {
    position: absolute;
    left: 8px;
    top: 648px;
    width: 140px;
    color: var(--white);
    font-weight: 400;
    font-size: 12.5px;
    line-height: 1.05;
    text-align: center;
    display: flex;
    align-items: center;
    justify-content: center;
    gap: 5px;
  }
  .footer-dot {
    width: 8px;
    height: 8px;
    border-radius: 50%;
    background: var(--white);
    flex: none;
  }
</style>
</head>
<body>
<div class="canvas">
  <div class="banner">
    <svg class="banner-shapes" viewBox="0 0 276 680" xmlns="http://www.w3.org/2000/svg">
      <defs>
        <linearGradient id="headerBlue" x1="0" y1="0" x2="1" y2="0.3">
          <stop offset="0" stop-color="#2a8fd6"/>
          <stop offset="1" stop-color="#163777"/>
        </linearGradient>
        <linearGradient id="photoTone" x1="0" y1="0" x2="1" y2="1">
          <stop offset="0" stop-color="#dfe3e3"/>
          <stop offset="0.45" stop-color="#c9a58e"/>
          <stop offset="0.7" stop-color="#eef0f0"/>
          <stop offset="1" stop-color="#9aa2a6"/>
        </linearGradient>
        <linearGradient id="roomTone" x1="0" y1="0" x2="0" y2="1">
          <stop offset="0" stop-color="#f4f5f5"/>
          <stop offset="1" stop-color="#d9dcdc"/>
        </linearGradient>
        <linearGradient id="redCorner" x1="0" y1="0" x2="1" y2="1">
          <stop offset="0" stop-color="#c21d33"/>
          <stop offset="1" stop-color="#8e0f20"/>
        </linearGradient>
      </defs>

      <!-- header band -->
      <path d="M0 0 H276 V52 C200 48 120 66 0 96 Z" fill="url(#headerBlue)"/>
      <path d="M0 96 C120 66 200 48 276 52 V60 C200 58 120 76 0 104 Z" fill="#ffffff"/>
      <path d="M0 104 C120 76 200 58 276 60 V63 C200 62 120 80 0 107 Z" fill="#1f7fc6"/>

      <!-- photograph area -->
      <rect x="0" y="178" width="276" height="262" fill="url(#photoTone)" role="img" aria-label="Photo: cardiologist monitoring a patient wearing ECG electrodes during a stress test"/>

      <!-- lower room backdrop -->
      <path d="M0 430 C90 420 190 440 276 470 V680 H0 Z" fill="url(#roomTone)" role="img" aria-label="Soft background photo of a bright clinic room"/>

      <!-- red swoosh divider -->
      <path d="M0 428 C80 414 180 432 276 462 V470 C180 442 80 424 0 436 Z" fill="#b3172c"/>
      <path d="M0 436 C80 424 180 442 276 470 V476 C180 450 80 432 0 442 Z" fill="#ffffff"/>

      <!-- red corner -->
      <path d="M0 585 L150 680 H0 Z" fill="url(#redCorner)"/>
    </svg>

    <div class="brand-name"><span class="brand-dot"></span><span>BRAMLEY CARDIAC<br>CENTRE</span></div>

    <ul class="service-list">
      <li>Echocardiogram</li>
      <li>Stress Echocardiogram</li>
      <li>Holter/Loop Monitor</li>
      <li>Ambulatory Blood<br>Pressure Monitoring</li>
      <li>Electrocardiogram</li>
      <li>Cardiac Consultations</li>
    </ul>

    <div class="footer-name"><span class="footer-dot"></span><span>BRAMLEY CARDIAC<br>CENTRE</span></div>
  </div>
</div>
</body>
</html>
```